Web Design for One for One Organic Soap Company

We need a website design for the company Tidewell Botanics based on the package design per attached.

The design should communicate high end, luxury organic. The site will provide facts about how the spread of disease causes deaths and can be prevented with hand washing. The site will also have a page about why we are passionate about organics and how that relates to our skin including skin facts.
Also, the site should have an e-commerce product page and shopping cart.

Target Market(s)

Educated, health conscious and socially conscious consumers who shop luxury. Target vendors include Larkmont Grocers and Velbrook..

Industry/Entity Type

E-Commerce

Font styles to use
Other font styles liked:
• See attached

Requirements
Must have
• Use of Ying Yang leaf Logo provided.
Based on design provided.

```html
<!DOCTYPE html>
<html lang="en">
<head>
<meta charset="utf-8">
<title>Tidewell Botanics — Home</title>
<link href="https://fonts.googleapis.com/css2?family=Open+Sans:wght@400;600;700&family=Oswald:wght@500;600&display=swap" rel="stylesheet">
<style>
  :root {
    --tan: #d8c2a0;
    --brown: #3f2a17;
    --rust: #a63b22;
    --red: #e2474b;
    --teal: #4fd0d6;
    --sky: #8fd5ea;
    --sun: #f3d28c;
    --ink: #333333;
    --muted: #888888;
    --line: #e6e6e6;
    --white: #ffffff;
  }
  * { box-sizing: border-box; margin: 0; padding: 0; }
  html, body { width: 1200px; height: 800px; overflow: hidden; }
  body {
    background: var(--tan);
    font-family: "Open Sans", Arial, sans-serif;
    color: var(--ink);
  }
  .page {
    width: 1000px; height: 800px; margin: 0 auto;
    background: var(--white);
    display: flex; flex-direction: column;
  }
  .account-bar {
    display: flex; justify-content: flex-end; gap: 14px;
    padding: 10px 24px 0; font-size: 11px; color: var(--muted);
  }
  .account-bar .sep { color: #bbb; }
  .account-bar .cart { display: flex; align-items: center; gap: 5px; }
  .site-header {
    display: flex; align-items: center; padding: 12px 24px 0; height: 76px;
  }
  .brand { display: flex; align-items: center; gap: 10px; width: 310px; }
  .brand-square { width: 34px; height: 34px; background: var(--rust); flex: none; }
  .brand-name { font-size: 20px; font-weight: 600; color: var(--brown); white-space: nowrap; }
  .perks { display: flex; gap: 34px; }
  .perk { display: flex; align-items: center; gap: 10px; width: 200px; }
  .perk-icon {
    width: 34px; height: 34px; border-radius: 50%;
    display: flex; align-items: center; justify-content: center; flex: none;
  }
  .perk-icon.blue { background: var(--sky); }
  .perk-icon.gold { background: var(--sun); }
  .perk-title { font-family: "Oswald", sans-serif; font-size: 11px; font-weight: 600; color: var(--brown); text-transform: uppercase; white-space: nowrap; }
  .perk-text { font-size: 11px; color: var(--muted); white-space: nowrap; }
  .main-nav {
    display: flex; gap: 22px; padding: 18px 24px 14px;
    font-size: 11px; font-weight: 700; color: var(--brown); border-bottom: 1px solid var(--line);
  }
  .main-nav .active { color: var(--red); }
  .hero {
    position: relative; height: 320px;
    background: linear-gradient(100deg, #c9a98a 0%, #d8c0a6 22%, #b9d6ea 38%, #e6f1f8 65%, #a9cbe4 100%);
  }
  .hero-photo { position: absolute; inset: 0; }
  .hero-caption { position: absolute; left: 250px; top: 115px; }
  .slide-tag {
    display: inline-block; background: var(--teal); color: var(--white);
    font-family: "Oswald", sans-serif; font-size: 14px; font-weight: 500; padding: 5px 10px;
  }
  .slide-text {
    margin-top: 8px; width: 470px; background: rgba(255,255,255,0.75);
    font-size: 10px; color: #666; padding: 7px 10px; text-transform: uppercase;
  }
  .read-more {
    display: inline-block; margin-top: 10px; background: var(--red); color: var(--white);
    font-size: 10px; padding: 5px 12px;
  }
  .slide-arrow {
    position: absolute; top: 150px; width: 26px; height: 26px; background: var(--white);
    border: 1px solid #ccc; display: flex; align-items: center; justify-content: center;
  }
  .slide-arrow.next { right: 24px; }
  .slide-dot { position: absolute; right: 14px; top: 12px; width: 6px; height: 6px; border-radius: 50%; background: var(--red); }
  .tagline {
    text-align: center; padding: 18px 0;
    font-family: "Oswald", sans-serif; font-size: 15px; font-weight: 500; color: var(--brown);
    text-transform: uppercase;
  }
  .tagline em { font-style: normal; color: var(--red); }
  .features { display: flex; gap: 30px; padding: 0 40px; }
  .feature { flex: 1; text-align: center; display: flex; flex-direction: column; align-items: center; }
  .feature-media { height: 118px; width: 100%; }
  .feature-media.field { background: linear-gradient(#7cc2e8, #6fae3c 70%, #2e5a1c); }
  .feature-media.people { background: linear-gradient(#d7dfc6, #9aa77a 60%, #6a6f4a); }
  .feature-media.giving { background: linear-gradient(135deg, #f2c4c4, #c9e6e8 55%, #d4eabc); }
  .feature-title {
    margin-top: 10px; font-family: "Oswald", sans-serif; font-size: 13px; font-weight: 500;
    color: var(--brown); text-transform: uppercase;
  }
  .feature-text { margin-top: 4px; font-size: 11px; color: var(--muted); line-height: 1.45; white-space: nowrap; }
  .feature .read-more { background: var(--rust); }
</style>
</head>
<body>
<div class="page">
  <div class="account-bar">
    <span>My Account</span><span class="sep">|</span>
    <span>Wishlist</span><span class="sep">|</span>
    <span>Check Out</span><span class="sep">|</span>
    <span>Log in</span>
    <span class="cart">
      <svg width="12" height="11" viewBox="0 0 12 11"><path d="M0 1h2l2 6h6l2-5H3" fill="none" stroke="#555" stroke-width="1.3"/><circle cx="5" cy="9.5" r="1" fill="#555"/><circle cx="9" cy="9.5" r="1" fill="#555"/></svg>
      Cart empty Show Cart
    </span>
  </div>

  <header class="site-header">
    <div class="brand">
      <span class="brand-square"></span>
      <span class="brand-name">Tidewell Botanics</span>
    </div>
    <div class="perks">
      <div class="perk">
        <span class="perk-icon blue"><svg width="14" height="16" viewBox="0 0 14 16"><path d="M7 1C5 5 2 8 2 10.5a5 5 0 0 0 10 0C12 8 9 5 7 1z" fill="#fff"/></svg></span>
        <div><div class="perk-title">Money Back Guaranteed</div><div class="perk-text">Lorem ipsum dolor sit amet</div></div>
      </div>
      <div class="perk">
        <span class="perk-icon blue"><svg width="12" height="16" viewBox="0 0 12 16"><rect x="4" y="0" width="4" height="3" fill="#fff"/><rect x="2" y="4" width="8" height="11" rx="2" fill="#fff"/></svg></span>
        <div><div class="perk-title">Free Shipping Items</div><div class="perk-text">Lorem ipsum dolor sit amet</div></div>
      </div>
      <div class="perk">
        <span class="perk-icon gold"><svg width="16" height="16" viewBox="0 0 16 16"><path d="M4 1l3 3-2 2c1 2 3 4 5 5l2-2 3 3-2 3C7 14 2 9 1 3z" fill="#fff"/></svg></span>
        <div><div class="perk-title">Online Support 24/7</div><div class="perk-text">Lorem ipsum dolor sit amet</div></div>
      </div>
    </div>
  </header>

  <nav class="main-nav">
    <span class="active">HOME</span><span>SOAPS</span><span>BODY BUTTER</span><span>ONE FOR ONE</span>
    <span>SKING FACTS</span><span>BLOG</span><span>ABOUT US</span><span>CONTACTS</span>
  </nav>

  <section class="hero">
    <div class="hero-photo" role="img" aria-label="Photo of a smiling woman holding a pink gift box against a bright cloudy sky"></div>
    <span class="slide-dot"></span>
    <div class="hero-caption">
      <div class="slide-tag">SLIDE CONTENT 2</div>
      <div class="slide-text">Lorem ipsum dolor sit amet, consectetur adipiscing elit, sed do...</div>
      <span class="read-more">Read more...</span>
    </div>
    <span class="slide-arrow next"><svg width="8" height="10" viewBox="0 0 8 10"><path d="M2 1l4 4-4 4" fill="none" stroke="#555" stroke-width="1.5"/></svg></span>
  </section>

  <div class="tagline">Nunc eleifend nulla vel orci. Donec sollicitudin. <em>Stay tuned!</em></div>

  <section class="features">
    <article class="feature">
      <div class="feature-media field" role="img" aria-label="Photo of green seedlings in a sunny field"></div>
      <h3 class="feature-title">Organic Elements</h3>
      <p class="feature-text">Pure plant oils, gently pressed and slowly cured.</p>
      <span class="read-more">Read more</span>
    </article>
    <article class="feature">
      <div class="feature-media people" role="img" aria-label="Photo of a family gathered outdoors"></div>
      <h3 class="feature-title">Safe for Everyone</h3>
      <p class="feature-text">Mild enough for little hands and sensitive skin alike.</p>
      <span class="read-more">Read more</span>
    </article>
    <article class="feature">
      <div class="feature-media giving" role="img" aria-label="Illustration about giving back to families in need"></div>
      <h3 class="feature-title">Give Back</h3>
      <p class="feature-text">Every bar you buy sends one bar to a family in need.</p>
      <span class="read-more">Read more</span>
    </article>
  </section>
</div>
</body>
</html>
```